Irrigation Business needs their business cards modernised and revamped

I would like to keep my current logo, colours and revamp the format of the card.

I would like the card to be clean yet important.

Im not sure if you include texture but i would like the named logo to be indented into the card etc.

show me something alive and free something thats clinical to the point yet has a feel of achievement. i would like people to go nice card.

Target Market(s)

high end clients, corporate, sports field manger, the guys that make the decisions

Industry/Entity Type

Business

Contact Information for Business Card

nformation to be included

Dorian Hesk (Director)
0487253916
dorian@tfcraft.biz
www.taddsfieldcrafts.com

instagram logo
google logo
facebook logo

Colors

Designer to choose colors to be used in the design.

Requirements
Nice to have
• indentations a really nice feel to the card good texture

```html
<!DOCTYPE html>
<html lang="en">
<head>
<meta charset="utf-8">
<title>Tadd's Field Crafts – Business Card</title>
<link rel="stylesheet" href="https://fonts.googleapis.com/css2?family=Archivo:wght@700&family=Roboto+Condensed:wght@400;700&family=Questrial&display=swap">
<style>
  :root {
    --backdrop: #1c1c1e;
    --card: #f4f4f2;
    --navy: #0b4f98;
    --sky: #1a9bd0;
    --green: #1a8a3a;
    --ink: #2a2a2a;
  }
  * { margin: 0; padding: 0; box-sizing: border-box; }
  html, body {
    width: 1200px; height: 1001px; overflow: hidden;
    background: var(--backdrop);
  }
  .card {
    position: absolute; top: 362px;
    width: 508px; height: 276px;
    background: var(--card);
    border-radius: 26px;
    overflow: hidden;
  }
  .card--front { left: 70px; }
  .card--back { left: 622px; }

  .orb {
    position: absolute; top: -60px;
    width: 396px; height: 396px;
    border-radius: 50%;
    background: var(--sky);
    box-shadow: inset 0 0 0 22px var(--navy);
  }
  .card--front .orb { left: 332px; }
  .card--back .orb { left: -220px; }

  .brand {
    position: absolute; left: 0; width: 332px; top: 78px;
    text-align: center;
  }
  .brand__dot {
    display: block; margin: 0 auto 14px;
    width: 76px; height: 76px; border-radius: 50%;
    background: var(--navy);
  }
  .brand__name {
    font-family: "Archivo", sans-serif; font-weight: 700;
    font-size: 23px; color: var(--navy); letter-spacing: -0.3px;
  }

  .contact {
    position: absolute; right: 32px; top: 52px; text-align: right;
    font-family: "Questrial", sans-serif; color: var(--ink); font-size: 13px;
    line-height: 17px;
  }
  .contact__role {
    font-family: "Roboto Condensed", sans-serif; font-size: 15px;
    margin-bottom: 8px;
  }
  .contact__name { color: var(--navy); font-weight: 700; }
  .contact__title { color: var(--green); }
  .contact__sep { color: var(--green); margin: 0 6px; }

  .social {
    position: absolute; right: 32px; top: 196px; display: flex; gap: 6px;
  }
  .social__icon {
    width: 23px; height: 23px; border-radius: 3px; background: var(--sky);
  }
  .website {
    position: absolute; right: 32px; top: 228px;
    font-family: "Questrial", sans-serif; font-size: 13.5px; color: var(--ink);
    display: flex; align-items: center; gap: 8px;
  }
</style>
</head>
<body>
  <section class="card card--front">
    <div class="orb"></div>
    <div class="brand">
      <span class="brand__dot"></span>
      <div class="brand__name">TADD'S FIELD CRAFTS</div>
    </div>
  </section>

  <section class="card card--back">
    <div class="orb"></div>
    <div class="contact">
      <div class="contact__role"><span class="contact__name">DORIAN HESK</span><span class="contact__sep">/</span><span class="contact__title">DIRECTOR</span></div>
      <div>0487253916</div>
      <div>dorian@tfcraft.biz</div>
    </div>
    <div class="social">
      <span class="social__icon" role="img" aria-label="social profile"></span>
      <span class="social__icon" role="img" aria-label="social profile"></span>
      <span class="social__icon" role="img" aria-label="social profile"></span>
    </div>
    <div class="website">
      <svg width="6" height="11" viewBox="0 0 6 11" aria-hidden="true"><path d="M0 0 L6 5.5 L0 11 Z" fill="var(--sky)"/></svg>
      <span>www.taddsfieldcrafts.com</span>
    </div>
  </section>
</body>
</html>
```